DUN Meridian Safeguard Sell Sheet

We need a two-sided portrait-style sell sheet for a new insurance product called the DUN Meridian Safeguard. The DUN Meridian Safeguard is a custom Executive Risk commercial insurance policy that provides the broadest level of protection available in the marketplace. The sell sheet would primarily use the colors blue, gray and white, have clean lines, minimal graphics (perhaps a picture of an executive boardroom at the top), three boxes (or text areas) to provide a brief description of the specific insurance products provided by the Meridian (Directors & Officers Liability, Employment Practices Liability, and Fiduciary Liability), be easy to read and really pique the reader's interest to learn more about the product. The title (DUN Meridian Safeguard) would overlay the graphic at the top, and just below the title would be the phrase "Expect More", which is our tagline for the product. There would be a two-sentence lead-in phrase just below the graphic ("Meridian Safeguard is an exclusive, custom-designed insurance policy tailored to a company’s specific risk profile. The policy was created to provide clients with a premium, industry-leading level of protection not found in the standard insurance marketplace". There needs to be another text section entitled "Return on Investment" and capable of containing three medium length sentences. There needs to be an "About Us" section (three to four medium-length sentences) and a "Contact Us" section (contact name, phone (x2), e-mail, address). On the back we want to discuss the specific features of the product by section of the policy (General Terms and Conditions, Directors & Officers Liability Insurance, Employment Practices Liability Insurance, Fiduciary Liability Insurance. This would likely be set out in bullet format.

I have attached a few examples found on the web that are similar to my vision for this sell sheet, but none that exactly fit our needs (whether graphically or due to specific layout).

Insurance

Serif

• I have uploaded a sample done in powerpoint. Please disregard the coloring as I did not have time to choose colors. I did not add the "About Us" and "Contact Us" sections on the front page and would like creative ideas on structuring that. On the back page, I think a nice looking table broken down by section of the policy would look nice, and allow us to enter bulleted coverage features for each section. Both graphics in the sample were found on google without watermarks by searching "board room" and "business agreement", respectively.

```html
<!DOCTYPE html>
<html lang="en">
<head>
<meta charset="utf-8">
<title>DUN Meridian Safeguard Sell Sheet</title>
<link href="https://fonts.googleapis.com/css2?family=Source+Sans+3:wght@400;600;700&display=swap" rel="stylesheet">
<style>
:root{
  --stage:#d1d2d4;
  --blue:#1e9cd7;
  --band-blue:#1577b3;
  --charcoal:#333333;
  --paper:#ffffff;
  --panel:#f2f2f2;
  --ink:#3a3a3a;
  --light:#ffffff;
}
*{margin:0;padding:0;box-sizing:border-box}
html,body{width:1200px;height:864px;overflow:hidden}
body{background:var(--stage);font-family:"Source Sans 3",sans-serif;color:var(--ink);position:relative}
.top-strip{position:absolute;left:0;top:0;width:1200px;height:51px;background:var(--paper)}
.bottom-strip{position:absolute;left:0;bottom:0;width:1200px;height:4px;background:var(--paper)}
.page{position:absolute;top:126px;width:490px;height:634px;background:var(--paper);box-shadow:3px 4px 8px rgba(0,0,0,.35);overflow:hidden}
.front{left:94px}
.back{left:637px}
.abs{position:absolute}
.photo{position:absolute;left:0;top:0;width:100%}
.photo-boardroom{height:202px;background:linear-gradient(160deg,#f4f4f4 0%,#bdbdbd 35%,#6e6e6e 60%,#9a9a9a 80%,#3e3e3e 100%)}
.photo-signing{height:190px;background:linear-gradient(200deg,#e9e9e9 0%,#a9a9a9 40%,#d6d6d6 65%,#5a5a5a 100%)}

/* front */
.about-col{left:0;top:144px;width:245px;height:392px;background:var(--blue);color:var(--light)}
.about-title{position:absolute;left:11px;top:24px;font-size:9.5px;font-weight:700}
.about-text{position:absolute;left:11px;top:38px;width:225px;font-size:7.6px;line-height:10.4px;font-weight:600;text-align:justify}
.product{position:absolute;left:10px;width:230px}
.product-head{display:flex;align-items:center;gap:5px;font-size:7.8px;font-weight:700;letter-spacing:-.1px}
.icon-ring{width:37px;height:37px;border-radius:50%;border:1.6px solid var(--light);display:flex;align-items:center;justify-content:center;flex:none}
.icon-disc{width:30px;height:30px;border-radius:50%;background:var(--light);display:flex;align-items:center;justify-content:center}
.product ul{list-style:none;margin-top:5px;margin-left:4px}
.product li{font-size:7.8px;line-height:15.4px}
.product li::before{content:"• "}
.contact-col{left:0;top:536px;width:245px;height:98px;background:var(--charcoal);color:var(--light)}
.contact-name{position:absolute;left:13px;top:12px;font-size:13px;font-weight:400}
.contact-row{position:absolute;left:13px;display:flex;align-items:center;gap:8px;font-size:8px}
.dot{width:15px;height:15px;border-radius:50%;background:var(--blue);border:1px solid var(--light);display:flex;align-items:center;justify-content:center;flex:none}

.title-band{left:245px;top:144px;width:245px;height:58px;background:rgba(70,70,70,.88);color:var(--light);text-align:center}
.product-name{position:absolute;left:0;width:100%;top:4px;font-size:14px;font-weight:400;letter-spacing:.2px}
.tagline{position:absolute;left:10px;width:225px;top:22px;font-size:10px;display:flex;align-items:center;gap:8px}
.tagline::before,.tagline::after{content:"";flex:1;height:1px;background:var(--light)}
.strap{position:absolute;left:0;width:100%;top:36px;font-size:10px}
.strap u{text-underline-offset:1px}
.story-col{left:245px;top:202px;width:245px;height:432px;background:var(--panel)}
.story{position:absolute;left:11px;width:222px;font-size:7.7px;line-height:10.4px;text-align:justify}
.story-bar{position:absolute;left:0;height:13px;background:var(--charcoal);color:var(--light);font-size:8.2px;font-weight:600;padding-left:11px;line-height:13px}

/* back */
.coverage-band{left:0;top:152px;width:100%;height:50px;background:rgba(21,119,179,.92);color:var(--light);font-size:15px;text-align:center;line-height:50px}
.col-panel{position:absolute;top:222px;width:155px;height:350px;background:var(--panel)}
.col-head{position:absolute;width:155px;height:30px;background:var(--charcoal);color:var(--light);font-size:10.4px;text-align:center;line-height:30px;white-space:nowrap}
.col-list{position:absolute;list-style:none;width:155px;padding-left:3px}
.col-list li{font-size:7.6px;line-height:15.2px;white-space:nowrap}
.col-list li::before{content:"• "}
.back-footer{left:0;top:586px;width:100%;height:48px;background:var(--charcoal);color:var(--light)}
.back-footer .contact-row{top:16px;font-size:8.4px}
</style>
</head>
<body>
<div class="top-strip"></div>
<div class="bottom-strip"></div>

<!-- Front side -->
<section class="page front">
  <div class="photo photo-boardroom" role="img" aria-label="Black and white photo of an empty boardroom table lined with leather chairs"></div>

  <div class="abs about-col">
    <h2 class="about-title">ABOUT US</h2>
    <p class="about-text">This is a sample version of Lorem Ipsum. Proin gravida nibh vel velit auctor aliquet. Aenean sollicitudin, lorem quis bibendum auctor, nisi elit consequat ipsum, nec sagittis sem nibh id elit. Duis sed odio sit amet nibh vulputate cursus a sit amet mauris. Morbi accumsan ipsum velit. Nam nec tellus a odio tincidunt auctor a ornare odio. Sed non mauris vitae erat consequat auctor eu in elit.</p>

    <div class="product" style="top:119px">
      <div class="product-head">
        <span class="icon-ring"><span class="icon-disc">
          <svg width="16" height="16" viewBox="0 0 16 16"><rect x="3" y="2.5" width="10" height="12" rx="1" fill="none" stroke="#1e9cd7" stroke-width="1.4"/><rect x="6" y="1.2" width="4" height="2.6" fill="#1e9cd7"/><path d="M5 8.5l2 2 4-4" fill="none" stroke="#1e9cd7" stroke-width="1.4"/></svg>
        </span></span>
        DIRECTORS &amp; OFFICERS LIABILITY INSURANCE
      </div>
      <ul><li>This is one line of text that will be used in the document</li><li>This is one line of text that will be used in the document</li><li>This is one line of text that will be used in the document</li></ul>
    </div>

    <div class="product" style="top:212px">
      <div class="product-head">
        <span class="icon-ring"><span class="icon-disc">
          <svg width="18" height="16" viewBox="0 0 18 16"><circle cx="5" cy="5" r="2.2" fill="#1e9cd7"/><circle cx="13" cy="5" r="2.2" fill="#1e9cd7"/><circle cx="9" cy="7" r="2.4" fill="#1e9cd7"/><path d="M1 13a4 4 0 0 1 8 0zM9 13a4 4 0 0 1 8 0z" fill="#1e9cd7"/><path d="M4.5 15a4.5 4.5 0 0 1 9 0z" fill="#1e9cd7"/></svg>
        </span></span>
        EMPLOYMENT PRACTICES LIABILITY INSURANCE
      </div>
      <ul><li>This is one line of text that will be used in the document</li><li>This is one line of text that will be used in the document</li><li>This is one line of text that will be used in the document</li></ul>
    </div>

    <div class="product" style="top:305px">
      <div class="product-head">
        <span class="icon-ring"><span class="icon-disc">
          <svg width="18" height="12" viewBox="0 0 18 12"><path d="M1 4l4-2 4 3 4-3 4 2-5 6-3-2-3 2z" fill="#1e9cd7"/></svg>
        </span></span>
        FIDUCIARY LIABILITY INSURANCE
      </div>
      <ul><li>This is one line of text that will be used in the document</li><li>This is one line of text that will be used in the document</li><li>This is one line of text that will be used in the document</li></ul>
    </div>
  </div>

  <div class="abs contact-col">
    <p class="contact-name">Your Name - your title</p>
    <div class="contact-row" style="top:35px"><span class="dot"><svg width="8" height="8" viewBox="0 0 8 8"><path d="M2 1l1.3 1.6-.7 1a4 4 0 0 0 1.8 1.8l1-.7L7 6 6 7.2C3.5 7 1 4.5.8 2z" fill="#fff"/></svg></span>000 000 0000</div>
    <div class="contact-row" style="top:56px"><span class="dot"><svg width="9" height="7" viewBox="0 0 9 7"><rect x=".5" y=".5" width="8" height="6" fill="#fff"/><path d="M.5.5l4 3.2 4-3.2" fill="none" stroke="#1e9cd7" stroke-width=".8"/></svg></span>dunmeridian@mailbox.net</div>
    <div class="contact-row" style="top:76px"><span class="dot"><svg width="9" height="9" viewBox="0 0 9 9" fill="none" stroke="#fff" stroke-width=".8"><circle cx="4.5" cy="4.5" r="3.8"/><ellipse cx="4.5" cy="4.5" rx="1.7" ry="3.8"/><path d="M.7 4.5h7.6"/></svg></span>www.dunmeridian.com</div>
  </div>

  <div class="abs title-band">
    <h1 class="product-name">MERIDIAN SAFEGUARD</h1>
    <p class="tagline">EXPECT MORE</p>
    <p class="strap"><u>“Industry-leadi</u>ng protection for <u>Executive Risk.”</u></p>
  </div>

  <div class="abs story-col">
    <p class="story" style="top:22px">Meridian Safeguard was created to address the market’s growing need for a premium Executive Risk insurance policy. Current solutions vary substantially in the coverage provided and limitations imposed. Despite an abundance of capacity, even recent new-to-market solutions contain trade-offs with respect to the policy’s terms and conditions.</p>
    <p class="story" style="top:93px">Insurance agents and buyers face challenging decisions often requiring meaningful sacrifices to coverage when selecting one policy over another. Meridian Safeguard is changing Executive Risk insurance by combining the industry’s most sought-after enhancements into a single, best-in-class solution.</p>
    <div class="story-bar" style="top:171px;width:218px">RISK MANAGEMENT RETURN ON INVESTMENT</div>
    <p class="story" style="top:192px">We view insurance premiums not as a cost of doing business, but rather as an investment in their risk management. A long-term approach is strongly recommended, rather than trying to ‘time the market’ with respect to the manifestation of a “Claim”. The policy’s language at the time of a “Claim” will determine the portion of loss covered by the policy. Therefore, breadth of coverage, rather than the cost of the policy (i.e. premium), is the recommended focal point to maximize risk management return on investment.</p>
    <div class="story-bar" style="top:300px;width:195px">KNOW THE SCORE</div>
    <p class="story" style="top:321px">Admittedly it can be difficult to compare two or more insurance proposals. In any comparison there are both objective and subjective factors to consider and weigh appropriately. Our Policy Strength Index (“PSI”) helps to reduce those comparisons to two numbers: (i) an index score based on common terms and conditions of Executive Risk insurance policies, and (ii) a risk-specific score based on a particular client’s risk profile. PSI helps to ensure clients are getting the best protection to suit their specific insurance needs.</p>
  </div>
</section>

<!-- Back side -->
<section class="page back">
  <div class="photo photo-signing" role="img" aria-label="Black and white photo of a hand holding a pen over a document"></div>
  <div class="abs coverage-band">COVERAGE HIGHLIGHTS</div>

  <div class="col-panel" style="left:6px"></div>
  <div class="col-panel" style="left:167px"></div>
  <div class="col-panel" style="left:329px"></div>

  <div class="col-head" style="left:6px;top:222px">General Terms &amp; Conditions</div>
  <div class="col-head" style="left:167px;top:222px">Directors &amp; Officers Liability</div>
  <div class="col-head" style="left:329px;top:222px;font-size:10.2px">Employment Practices Liability</div>
  <div class="col-head" style="left:329px;top:406px">Fiduciary Liability</div>

  <ul class="col-list" style="left:6px;top:258px">
    <li>This is one line of text that will be used</li><li>This is one line of text that will be used</li><li>This is one line of text that will be used</li><li>This is one line of text that will be used</li><li>This is one line of text that will be used</li><li>This is one line of text that will be used</li><li>This is one line of text that will be used</li><li>This is one line of text that will be used</li><li>This is one line of text that will be used</li><li>This is one line of text that will be used</li><li>This is one line of text that will be used</li><li>This is one line of text that will be used</li><li>This is one line of text that will be used</li><li>This is one line of text that will be used</li><li>This is one line of text that will be used</li><li>This is one line of text that will be used</li><li>This is one line of text that will be used</li><li>This is one line of text that will be used</li><li>This is one line of text that will be used</li><li>This is one line of text that will be used</li>
  </ul>
  <ul class="col-list" style="left:167px;top:258px">
    <li>This is one line of text that will be used</li><li>This is one line of text that will be used</li><li>This is one line of text that will be used</li><li>This is one line of text that will be used</li><li>This is one line of text that will be used</li><li>This is one line of text that will be used</li><li>This is one line of text that will be used</li><li>This is one line of text that will be used</li><li>This is one line of text that will be used</li><li>This is one line of text that will be used</li><li>This is one line of text that will be used</li><li>This is one line of text that will be used</li><li>This is one line of text that will be used</li><li>This is one line of text that will be used</li><li>This is one line of text that will be used</li><li>This is one line of text that will be used</li><li>This is one line of text that will be used</li><li>This is one line of text that will be used</li><li>This is one line of text that will be used</li><li>This is one line of text that will be used</li>
  </ul>
  <ul class="col-list" style="left:329px;top:258px">
    <li>This is one line of text that will be used</li><li>This is one line of text that will be used</li><li>This is one line of text that will be used</li><li>This is one line of text that will be used</li><li>This is one line of text that will be used</li><li>This is one line of text that will be used</li><li>This is one line of text that will be used</li><li>This is one line of text that will be used</li><li>This is one line of text that will be used</li>
  </ul>
  <ul class="col-list" style="left:329px;top:441px">
    <li>This is one line of text that will be used</li><li>This is one line of text that will be used</li><li>This is one line of text that will be used</li><li>This is one line of text that will be used</li><li>This is one line of text that will be used</li><li>This is one line of text that will be used</li><li>This is one line of text that will be used</li><li>This is one line of text that will be used</li>
  </ul>

  <div class="abs back-footer">
    <div class="contact-row" style="left:21px"><span class="dot"><svg width="9" height="7" viewBox="0 0 9 7"><rect x=".5" y=".5" width="8" height="6" fill="#fff"/><path d="M.5.5l4 3.2 4-3.2" fill="none" stroke="#1e9cd7" stroke-width=".8"/></svg></span>dunmeridian@mailbox.net</div>
    <div class="contact-row" style="left:205px"><span class="dot"><svg width="8" height="8" viewBox="0 0 8 8"><path d="M2 1l1.3 1.6-.7 1a4 4 0 0 0 1.8 1.8l1-.7L7 6 6 7.2C3.5 7 1 4.5.8 2z" fill="#fff"/></svg></span>000 000 0000</div>
    <div class="contact-row" style="left:346px"><span class="dot"><svg width="9" height="9" viewBox="0 0 9 9" fill="none" stroke="#fff" stroke-width=".8"><circle cx="4.5" cy="4.5" r="3.8"/><ellipse cx="4.5" cy="4.5" rx="1.7" ry="3.8"/><path d="M.7 4.5h7.6"/></svg></span>www.dunmeridian.com</div>
  </div>
</section>
</body>
</html>
```